Business Card Design job - Tyre Shop

Client wants a double sided business cards designed for a Tyre Shop.

The logo can be used in multiple ways, some examples are attached.

The reference font is:
https://www.typebarrow.com/fonts/open-sans
Others can be applied.

Color scheme should be mainly black and white, and red as a third less used color.

Contact Information for Business Card

Required Fields (Portuguese language):
- Name "Augusto Melro"
- Title "Gerente"
- Phone "253 704 862"
- Website "www.rodaslume.pt"
- Email "geral@rodaslume.pt
- Address "Rua da Fonteira N.187
4920-318 Ribacova, Valmonte"

Font styles to use
Sans Serif

Requirements
Must have
• Corporate Logo
Nice to have
• The client would like the card to have special feature to measure the tyre tread, as shown in examples attached.
• The tread Values as Portuguese law are:
• - Ilegal - less than 1.6mm
• - change tyres - between 3mm and 1.6 mm
• - OK - above 3mm
• Card should be kept standard rectangle size 85x55mm

```html
<!DOCTYPE html>
<html lang="pt">
<head>
<meta charset="utf-8">
<title>Rodas Lume – Cartão de visita</title>
<link rel="stylesheet" href="https://fonts.googleapis.com/css2?family=Open+Sans:wght@400;600;700;800&display=swap">
<style>
  :root {
    --ink: #1a1a1a;
    --black: #000000;
    --white: #ffffff;
    --red: #ed1c24;
    --backdrop: #ececec;
  }
  * { box-sizing: border-box; margin: 0; padding: 0; }
  html, body {
    width: 1200px; height: 1200px; overflow: hidden;
    background: var(--backdrop);
    font-family: "Open Sans", Arial, sans-serif;
  }
  .card {
    position: absolute; left: 309px; width: 582px; height: 350px; overflow: hidden;
  }
  .card--front { top: 236px; background: var(--white); color: var(--ink); }
  .card--back { top: 634px; background: var(--black); color: var(--white); }

  .brand {
    position: absolute; left: 0; right: 0;
    display: flex; align-items: center; justify-content: center; gap: 14px;
  }
  .brand__mark { width: 28px; height: 28px; background: var(--ink); }
  .brand__name {
    font-weight: 800; font-size: 50px; letter-spacing: 0.5px; line-height: 1;
    color: var(--ink); white-space: nowrap;
  }
  .card--front .brand { top: 52px; }
  .card--back .brand { top: 149px; }
  .card--back .brand__mark { width: 34px; height: 34px; background: var(--white); }
  .card--back .brand__name { color: var(--white); font-size: 54px; }

  .person {
    position: absolute; right: 333px; top: 212px; text-align: right; white-space: nowrap;
  }
  .person__name { font-weight: 700; font-size: 29px; line-height: 1.1; }
  .person__role { font-weight: 400; font-size: 19px; line-height: 1.3; }

  .divider {
    position: absolute; left: 272px; top: 186px; width: 2px; height: 94px; background: var(--ink);
  }
  .contact {
    position: absolute; left: 292px; top: 188px; font-size: 15px; line-height: 18px; white-space: nowrap;
  }
  .contact__address { margin-bottom: 18px; }
  .contact strong { font-weight: 700; }

  .speed-bar {
    position: absolute; left: 0; display: flex; align-items: center;
  }
  .card--front .speed-bar { top: 323px; height: 12px; }
  .speed-bar__line { width: 515px; height: 100%; background: var(--red); }
  .speed-bar__arrows { height: 100%; margin-left: 3px; }

  .card--back .speed-bar { top: 304px; height: 31px; }
  .card--back .speed-bar__line {
    width: 495px; display: flex; align-items: center; justify-content: center;
    padding-left: 90px;
  }
  .website {
    color: var(--white); font-weight: 600; font-size: 16px; letter-spacing: 11px; white-space: nowrap;
  }
</style>
</head>
<body>

<section class="card card--front" aria-label="Frente do cartão">
  <div class="brand">
    <span class="brand__mark"></span>
    <span class="brand__name">RODAS LUME</span>
  </div>

  <div class="person">
    <p class="person__name">Augusto Melro</p>
    <p class="person__role">Gerente</p>
  </div>

  <div class="divider"></div>

  <div class="contact">
    <p class="contact__address">Rua da Fonteira N.187<br>4920-318 Ribacova, Valmonte</p>
    <p><strong>Phone:</strong> 253 704 862</p>
    <p><strong>Email:</strong> geral@rodaslume.pt</p>
  </div>

  <div class="speed-bar">
    <div class="speed-bar__line"></div>
    <svg class="speed-bar__arrows" width="36" height="12" viewBox="0 0 36 12">
      <g fill="#ed1c24">
        <polygon points="0,0 4,0 9,6 4,12 0,12 5,6"/>
        <polygon points="9,0 13,0 18,6 13,12 9,12 14,6"/>
        <polygon points="18,0 22,0 27,6 22,12 18,12 23,6"/>
        <polygon points="27,0 31,0 36,6 31,12 27,12 32,6"/>
      </g>
    </svg>
  </div>
</section>

<section class="card card--back" aria-label="Verso do cartão">
  <div class="brand">
    <span class="brand__mark"></span>
    <span class="brand__name">RODAS LUME</span>
  </div>

  <div class="speed-bar">
    <div class="speed-bar__line"><span class="website">www.rodaslume.pt</span></div>
    <svg class="speed-bar__arrows" width="54" height="31" viewBox="0 0 54 30">
      <g fill="#ed1c24">
        <polygon points="0,0 7,0 16,15 7,30 0,30 9,15"/>
        <polygon points="19,0 26,0 35,15 26,30 19,30 28,15"/>
        <polygon points="38,0 45,0 54,15 45,30 38,30 47,15"/>
      </g>
    </svg>
  </div>
</section>

</body>
</html>
```